Glow Jam - Concert Poster

We need a poster for a concert involving 3 bands. Marvolin, Auntie's Pickles and Velvet Hank. The event is called the Glow Jam. The poster will be a take away. We plan to print some to give out and some for advertising. Should be something people will want to put up on a wall. The poster should have a psychedelic "flavor", colorful.
Info. that needs to be on the poster: Glow Jam - Band Names - Bartleby's Sound Lodge - 4183 Route 12, Felton CA - $10 advance Tix - $12 at Door - for tickets www.bartlebyssound. - 21 and Over - March 21 2015 - Doors open at 7:00.

```html
<!DOCTYPE html>
<html lang="en">
<head>
<meta charset="utf-8">
<title>Glow Jam – Concert Poster</title>
<link rel="stylesheet" href="https://fonts.googleapis.com/css2?family=Chewy&family=Righteous&family=Gochi+Hand&family=Lobster&family=Alfa+Slab+One&family=Mouse+Memoirs&display=swap">
<style>
  :root {
    --page: #ffffff;
    --paper: #fbf8ea;
    --shadow: #9a9a9a;
    --orange: #f15a24;
    --gold: #f5d21a;
    --gold-edge: #8a6d00;
    --red: #c8202f;
    --ink: #1a1a1a;
    --blue: #23378f;
    --lens-light: #4a4a4a;
    --lens-dark: #0e0e0e;
    --glow: #fff21c;
    --daisy: #f1eee4;
    --aster: #7f97e6;
  }
  * { margin: 0; padding: 0; box-sizing: border-box; }
  html, body { width: 900px; height: 1200px; overflow: hidden; background: var(--page); }
  .poster {
    position: absolute; left: 22px; top: 20px; width: 856px; height: 1160px;
    background: var(--paper);
    box-shadow: 4px 4px 6px var(--shadow);
    overflow: hidden;
  }
  .line { position: absolute; left: 0; right: 0; text-align: center; white-space: nowrap; }

  .aster { position: absolute; left: 38px; top: 4px; width: 84px; height: 64px; border-radius: 50%; background: var(--aster); }
  .date {
    top: 0; left: 70px;
    font-family: "Alfa Slab One", serif; font-size: 62px; letter-spacing: 12px;
    color: var(--orange);
    -webkit-text-stroke: 1.5px var(--gold);
  }
  .date-rule { position: absolute; left: 150px; top: 74px; width: 670px; height: 6px; background: var(--orange); }

  .venue-at { position: absolute; left: 52px; top: 108px; font-family: "Lobster", cursive; font-size: 44px; color: var(--red); }
  .venue-name { top: 140px; left: 40px; font-family: "Lobster", cursive; font-size: 54px; color: var(--red); }
  .venue-address { top: 206px; left: 0; font-family: "Gochi Hand", cursive; font-size: 42px; color: var(--ink); letter-spacing: 1px; }

  .shades-art {
    position: absolute; left: 18px; top: 280px; width: 800px; height: 265px;
    border-radius: 130px;
    background: radial-gradient(ellipse at 50% 55%, var(--lens-light) 0%, #1c1c1c 55%, var(--lens-dark) 100%);
  }
  .event-title {
    position: absolute; top: 318px;
    font-family: "Chewy", cursive; font-size: 150px; line-height: 1;
    color: var(--glow);
    text-shadow: 0 0 8px rgba(255, 242, 28, 0.7);
  }
  .event-title-1 { left: 40px; width: 380px; text-align: center; }
  .event-title-2 { left: 440px; width: 380px; text-align: center; }

  .featuring { top: 574px; left: -20px; font-family: "Gochi Hand", cursive; font-size: 48px; color: var(--ink); }
  .featuring span { border-bottom: 3px solid var(--ink); padding: 0 2px; }
  .doors { position: absolute; left: 34px; top: 596px; transform: rotate(-22deg); text-align: center; font-family: "Righteous", sans-serif; color: var(--ink); line-height: 0.8; }
  .doors b { display: block; font-weight: 400; font-size: 50px; }
  .doors small { font-size: 22px; }
  .time { position: absolute; left: 640px; top: 612px; transform: rotate(28deg); font-family: "Righteous", sans-serif; font-size: 54px; color: var(--ink); }

  .band { font-family: "Righteous", sans-serif; font-size: 46px; letter-spacing: 2px; }
  .band-1 { top: 650px; left: -20px; color: var(--ink); }
  .band-2 { top: 728px; left: -20px; color: var(--red); }
  .band-joiner { top: 800px; left: -20px; color: var(--red); }
  .band-3 { top: 876px; left: -20px; color: var(--blue); }

  .daisy { position: absolute; top: 724px; width: 190px; height: 190px; border-radius: 50%; background: var(--daisy); }
  .daisy-left { left: 14px; }
  .daisy-right { left: 650px; }

  .price { font-family: "Righteous", sans-serif; font-size: 50px; letter-spacing: 6px; color: var(--gold); -webkit-text-stroke: 1.5px var(--gold-edge); line-height: 1; }
  .price-advance { top: 944px; left: -10px; }
  .price-door { top: 990px; left: -20px; }
  .tickets { top: 1044px; left: 0; font-family: "Mouse Memoirs", sans-serif; font-size: 50px; letter-spacing: 2px; color: var(--ink); }
  .age { top: 1100px; left: -20px; font-family: "Alfa Slab One", serif; font-size: 42px; letter-spacing: 3px; color: var(--orange); }
</style>
</head>
<body>
<main class="poster">
  <div class="aster" role="img" aria-label="Blue aster flower decoration"></div>
  <div class="line date">March 21 2015</div>
  <div class="date-rule"></div>

  <div class="venue-at">At</div>
  <div class="line venue-name">Bartleby's Sound Lodge</div>
  <div class="line venue-address">4183 Route 12, &nbsp;Felton CA</div>

  <div class="shades-art" role="img" aria-label="Illustration of round black sunglasses framing the event title"></div>
  <h1 class="event-title event-title-1">Glow</h1>
  <div class="event-title event-title-2">Jam</div>

  <div class="doors"><b>Doors</b><small>open</small></div>
  <div class="line featuring"><span>Featuring</span></div>
  <div class="time">at 7:00</div>

  <div class="daisy daisy-left" role="img" aria-label="White daisy flower decoration"></div>
  <div class="daisy daisy-right" role="img" aria-label="White daisy flower decoration"></div>

  <div class="line band band-1">Marvolin</div>
  <div class="line band band-2">Auntie's Pickles</div>
  <div class="line band band-joiner">and</div>
  <div class="line band band-3">Velvet Hank</div>

  <div class="line price price-advance">$10 advance Tix</div>
  <div class="line price price-door">$12 at Door</div>
  <div class="line tickets">For tickets visit www.bartlebyssound.com</div>
  <div class="line age">21 and Over</div>
</main>
</body>
</html>
```